Award-winnning Estate Agent needs a premium version of their 'For Sale' board design

We need a premium option for our 'For Sale' board design. We have a standard board that is attached to this brief, but were are looking to have a premium design version that we will use when selling exclusive properties. Our company name is Harbour Lane Estates and the name for this is exclusive selection is: 'The Harbour Collection'. The design needs to work with our current brand, but have a distinctive PREMIUM feel to it. I have uploaded the barnd guidelines and also some of the exisisting logo variations. We do NOT need a new logo but feel free to play around with colours, fonts, sizes etc. for the sign.

Target Market(s)

Property buyers & house hunters

Industry/Entity Type

Real Estate - Residential Property

Font styles to use
Sans Serif

Requirements
Must have
• A premium fee, must be square design, must be easy to read when driving past the sign
Nice to have
• I'm open ot ideas

```html
<!DOCTYPE html>
<html lang="en">
<head>
<meta charset="utf-8">
<title>Harbour Lane Estates – For Sale Boards</title>
<link rel="stylesheet" href="https://fonts.googleapis.com/css2?family=Arimo:wght@700&family=Montserrat:wght@800;900&display=swap">
<style>
  :root {
    --gold-deep: #a47526;
    --gold-mid: #b98c3c;
    --gold-light: #d2af60;
    --gold-glow: #f5e7c8;
    --white: #ffffff;
    --page-top: #ebebeb;
    --page-bottom: #ffffff;
    --gold-sheen: linear-gradient(100deg, var(--gold-deep) 0%, var(--gold-mid) 25%, var(--gold-light) 47%, var(--gold-mid) 70%, var(--gold-deep) 100%);
    --gold-soft: linear-gradient(100deg, var(--gold-light) 0%, var(--gold-mid) 30%, var(--gold-light) 55%, var(--gold-mid) 80%, var(--gold-light) 100%);
  }
  * { box-sizing: border-box; margin: 0; padding: 0; }
  html, body { width: 1200px; height: 848px; overflow: hidden; }
  body {
    background: linear-gradient(180deg, var(--page-top) 0%, var(--page-bottom) 55%, var(--page-bottom) 100%);
    position: relative;
  }
  .board {
    position: absolute;
    top: 175px;
    width: 519px;
    height: 519px;
    background: var(--gold-sheen);
    padding: 19px;
  }
  .board--white-top { left: 66px; }
  .board--gold-top { left: 612px; }

  .board__brand {
    height: 228px;
    position: relative;
    display: flex;
    flex-direction: column;
    align-items: center;
    overflow: hidden;
  }
  .board--white-top .board__brand { background: var(--white); }

  .corner-glow {
    position: absolute;
    top: 0;
    width: 100px;
    height: 118px;
    background: linear-gradient(180deg, var(--gold-glow) 0%, rgba(245, 231, 200, 0) 100%);
  }
  .corner-glow--left { left: 0; clip-path: polygon(0 0, 100% 100%, 100% 100%, 0 100%); }
  .corner-glow--right { right: 0; clip-path: polygon(100% 0, 100% 100%, 0 100%, 0 100%); }

  .brand-mark {
    width: 92px;
    height: 92px;
    margin-top: 34px;
    position: relative;
  }
  .board--white-top .brand-mark { background: var(--gold-light); }
  .board--gold-top .brand-mark { background: var(--white); }

  .brand-name {
    font-family: "Arimo", Arial, sans-serif;
    font-weight: 700;
    font-size: 35px;
    letter-spacing: -0.3px;
    margin-top: 38px;
    white-space: nowrap;
    position: relative;
  }
  .board--white-top .brand-name { color: var(--gold-deep); }
  .board--gold-top .brand-name { color: var(--white); }

  .board__status {
    height: 103px;
    display: flex;
    align-items: center;
    justify-content: center;
  }
  .board--white-top .board__status { background: var(--gold-sheen); }
  .board--gold-top .board__status { background: var(--white); }

  .status-text {
    font-family: "Montserrat", sans-serif;
    font-weight: 900;
    font-size: 77px;
    letter-spacing: -3px;
    line-height: 1;
    white-space: nowrap;
  }
  .board--white-top .status-text { color: var(--white); }
  .board--gold-top .status-text {
    background: var(--gold-sheen);
    -webkit-background-clip: text;
    background-clip: text;
    color: transparent;
  }

  .board__phone {
    height: 89px;
    background: var(--gold-soft);
    display: flex;
    align-items: center;
    justify-content: center;
  }
  .phone-text {
    font-family: "Montserrat", sans-serif;
    font-weight: 800;
    font-size: 60px;
    letter-spacing: -2.5px;
    color: var(--white);
    line-height: 1;
    white-space: nowrap;
  }

  .board__web {
    height: 61px;
    background: var(--white);
    display: flex;
    align-items: center;
    justify-content: center;
  }
  .web-text {
    font-family: "Arimo", Arial, sans-serif;
    font-weight: 700;
    font-size: 25.5px;
    letter-spacing: -0.2px;
    color: var(--gold-deep);
    white-space: nowrap;
  }
</style>
</head>
<body>
  <section class="board board--white-top" aria-label="For sale board, white header">
    <div class="board__brand">
      <div class="corner-glow corner-glow--left"></div>
      <div class="corner-glow corner-glow--right"></div>
      <div class="brand-mark"></div>
      <p class="brand-name">Harbour Lane Estates</p>
    </div>
    <div class="board__status"><p class="status-text">FOR SALE</p></div>
    <div class="board__phone"><p class="phone-text">01632 960418</p></div>
    <div class="board__web"><p class="web-text">www.harbourlaneestates.co.uk</p></div>
  </section>

  <section class="board board--gold-top" aria-label="For sale board, gold header">
    <div class="board__brand">
      <div class="brand-mark"></div>
      <p class="brand-name">Harbour Lane Estates</p>
    </div>
    <div class="board__status"><p class="status-text">FOR SALE</p></div>
    <div class="board__phone"><p class="phone-text">01632 960418</p></div>
    <div class="board__web"><p class="web-text">www.harbourlaneestates.co.uk</p></div>
  </section>
</body>
</html>
```